For Tolvy: Business cards, letterhead, envelopes and double sided page

For Tolvy: Previously described in email.

Business cards, letterhead, envelopes, and glossy marketing double sided page.

Industry/Entity Type

Marketing

```html
<!DOCTYPE html>
<html lang="en">
<head>
<meta charset="utf-8">
<title>Tolvy — Business Card</title>
<link rel="stylesheet" href="https://fonts.googleapis.com/css2?family=Arimo:wght@400;700&display=swap">
<style>
  :root {
    --navy: #252a3f;
    --slate: #8a9fac;
    --white: #ffffff;
    --ink: #1d2030;
    --stage: #e9e7e3;
    --rule: #9aa0a8;
  }
  * { margin: 0; padding: 0; box-sizing: border-box; }
  html, body {
    width: 1200px; height: 843px; overflow: hidden;
    background: var(--stage);
    font-family: "Arimo", Arial, sans-serif;
  }
  .canvas { position: relative; width: 1200px; height: 843px; }
  .card {
    position: absolute; width: 620px; height: 354px; overflow: hidden;
    box-shadow: 0 6px 18px rgba(0,0,0,.18);
  }
  .card--front { left: 90px; top: 60px; background: var(--white); }
  .card--back  { left: 490px; top: 430px; background: var(--navy); }

  .brand { position: absolute; display: flex; align-items: center; gap: 18px; }
  .brand__mark { width: 66px; height: 66px; border-radius: 10px; }
  .brand__name { font-weight: 700; font-size: 78px; line-height: 1; letter-spacing: -1px; }
  .card--front .brand { left: 120px; top: 42px; }
  .card--front .brand__mark { background: var(--navy); }
  .card--front .brand__name { color: var(--navy); }
  .card--back .brand { left: 140px; top: 118px; }
  .card--back .brand__mark { background: var(--slate); }
  .card--back .brand__name { color: var(--slate); }

  .holder { position: absolute; left: 60px; top: 178px; width: 200px; text-align: center; color: var(--ink); }
  .holder__name { font-weight: 700; font-size: 20px; }
  .holder__title { font-size: 15px; margin-top: 4px; }

  .divider { position: absolute; left: 300px; top: 150px; width: 1px; height: 110px; background: var(--rule); }

  .contact-icons { position: absolute; left: 340px; top: 150px; display: flex; flex-direction: column; gap: 12px; }
  .contact-icons svg { width: 16px; height: 16px; display: block; }

  .bands { position: absolute; left: 0; bottom: 0; width: 620px; height: 110px; }

  .web { position: absolute; left: 222px; top: 212px; color: var(--slate); font-size: 15px; letter-spacing: .5px; }
</style>
</head>
<body>
<main class="canvas">
  <section class="card card--front" aria-label="Business card front">
    <div class="brand">
      <span class="brand__mark"></span>
      <span class="brand__name">Tolvy</span>
    </div>
    <div class="holder">
      <p class="holder__name">Name</p>
      <p class="holder__title">Executive Director</p>
    </div>
    <span class="divider"></span>
    <div class="contact-icons">
      <svg viewBox="0 0 16 16" aria-label="Mobile"><rect x="3" y="0.5" width="10" height="15" rx="2" fill="#252a3f"/><rect x="5" y="2.5" width="6" height="9" fill="#fff"/></svg>
      <svg viewBox="0 0 16 16" aria-label="Fax"><rect x="1" y="2" width="14" height="12" rx="2" fill="#252a3f"/><rect x="3.5" y="5" width="9" height="5" fill="#fff"/></svg>
      <svg viewBox="0 0 16 16" aria-label="Email"><circle cx="8" cy="8" r="7.5" fill="#252a3f"/><circle cx="8" cy="8" r="3.5" fill="none" stroke="#fff" stroke-width="1.6"/></svg>
      <svg viewBox="0 0 16 16" aria-label="Address"><rect x="0.5" y="0.5" width="15" height="15" rx="2" fill="#252a3f"/><path d="M8 3a3 3 0 0 1 3 3c0 2.3-3 6-3 6S5 8.3 5 6a3 3 0 0 1 3-3z" fill="#fff"/></svg>
    </div>
    <svg class="bands" viewBox="0 0 620 110" preserveAspectRatio="none" aria-hidden="true">
      <rect x="0" y="58" width="620" height="52" fill="#8a9fac"/>
      <polygon points="338,110 352,62 366,70 378,42 620,22 620,110" fill="#252a3f"/>
    </svg>
  </section>

  <section class="card card--back" aria-label="Business card back">
    <div class="brand">
      <span class="brand__mark"></span>
      <span class="brand__name">Tolvy</span>
    </div>
    <p class="web">www.tolvy.com</p>
  </section>
</main>
</body>
</html>
```